Calloway Holdings Website Design

We are a private equity firm based with offices based in Hong Kong, Singapore, London and Paris. Our focus is investments in property development projects, corporate ventures and loans.

We require the development of a new website and you will have to select relevant images from the likes of PixelVaultPics or other stock photo libraries.

We will need a design done for a PC based website and the designer selected with the favored design will also need to produce some concepts for a responsive website.

Target Market(s)

Sophisticated investors looking to invest in high return property development, businesses and mortgages.

Industry/Entity Type

Investment

Number of Pages Required

5+ page

Font styles to use
Serif
Sans Serif

Colors
0255a3
00a990

Requirements
Must have
• Clean modern feel and must portray stability and professionalism.

```html
<!DOCTYPE html>
<html lang="en">
<head>
<meta charset="utf-8">
<title>Calloway Holdings</title>
<link href="https://fonts.googleapis.com/css2?family=Arvo:wght@400;700&family=Arimo:wght@400;700&display=swap" rel="stylesheet">
<style>
:root{
  --blue:#0255a3;
  --navy:#1b2a4a;
  --teal:#00a990;
  --grey:#f0f0f0;
  --footer:#ebebeb;
  --dark:#2b2c30;
  --text:#555;
  --white:#fff;
}
*{margin:0;padding:0;box-sizing:border-box}
html,body{width:1200px;height:3429px;overflow:hidden}
body{font-family:"Arimo",Arial,sans-serif;color:var(--text);background:var(--white)}
.serif{font-family:"Arvo",Georgia,serif}
section,header,footer{position:relative;width:1200px}
.notch{position:absolute;left:50%;width:0;height:0;border-left:32px solid transparent;border-right:32px solid transparent;transform:translateX(-50%);z-index:2}

/* hero */
.hero{height:571px;background:linear-gradient(100deg,#c9d3dc 0%,#8a9aab 40%,#3c4a5e 70%,#1e2838 100%);overflow:hidden}
.hero-photo{position:absolute;inset:0;background:linear-gradient(90deg,rgba(230,236,242,.6) 0%,rgba(120,140,165,.3) 45%,rgba(30,38,52,.5) 75%,rgba(20,26,36,.7) 100%)}
.nav{position:absolute;top:0;left:0;right:0;height:73px;background:rgba(2,55,120,.85);display:flex;justify-content:center;align-items:center;gap:0}
.nav a{font-family:"Arvo",Georgia,serif;color:var(--white);text-decoration:none;font-size:15px;letter-spacing:.5px;margin:0 28px;padding-bottom:8px;border-bottom:2px solid transparent}
.nav a.active{border-bottom-color:var(--white)}
.brand{position:absolute;top:190px;left:0;right:0;display:flex;justify-content:center;align-items:center;gap:18px}
.brand .dot{width:54px;height:54px;border-radius:50%;background:var(--navy)}
.brand span{font-family:"Arvo",Georgia,serif;font-weight:700;font-size:44px;color:var(--navy)}
.hero h1{position:absolute;top:386px;left:0;right:0;text-align:center;font-family:"Arvo",Georgia,serif;font-weight:400;font-size:50px;color:var(--white)}
.hero p{position:absolute;top:462px;left:310px;right:310px;text-align:center;font-size:15px;line-height:24px;color:var(--white)}

/* welcome */
.welcome{height:316px;background:var(--grey)}
.welcome .label{position:absolute;top:638px;top:67px;left:82px;font-family:"Arvo",Georgia,serif;font-size:17px;color:#333}
.welcome h2{position:absolute;top:98px;left:82px;font-family:"Arvo",Georgia,serif;font-weight:400;font-size:39px;color:var(--blue)}
.welcome p{position:absolute;top:163px;left:85px;width:680px;font-size:14px;line-height:26px}
.welcome .more{position:absolute;top:253px;left:88px;font-family:"Arvo",Georgia,serif;font-size:13px;font-style:italic;font-weight:700;color:#222;text-decoration:underline}
.welcome .mark{position:absolute;top:138px;left:820px;font-family:"Arvo",Georgia,serif;font-weight:700;font-size:32px;color:var(--navy)}
.welcome .notch{bottom:-32px;border-top:32px solid var(--grey)}

/* features */
.features{height:475px;background:var(--white)}
.feature{position:absolute;top:77px;width:330px;text-align:center}
.feature .icon{width:128px;height:128px;margin:0 auto;border-radius:50%;border:2px solid #555;display:flex;align-items:center;justify-content:center}
.feature .icon.filled{background:var(--blue);border-color:var(--blue)}
.feature h3{margin-top:30px;font-family:"Arvo",Georgia,serif;font-weight:400;font-size:17px;color:#333}
.feature h3.accent{color:var(--blue)}
.feature p{margin:10px auto 0;width:290px;font-size:13px;line-height:27px;color:#333}
.btn{position:absolute;left:521px;width:158px;height:52px;background:var(--blue);color:var(--white);font-family:"Arvo",Georgia,serif;font-size:15px;display:flex;align-items:center;justify-content:center}
.features .btn{top:359px}

/* services */
.services{height:615px;background:linear-gradient(180deg,#3a3b40 0%,var(--dark) 50%,#1f2024 100%)}
.services .notch{top:0;border-top:32px solid var(--white)}
.services .kicker{position:absolute;top:75px;left:0;right:0;text-align:center;font-family:"Arvo",Georgia,serif;font-size:17px;color:var(--white)}
.services h2{position:absolute;top:106px;left:0;right:0;text-align:center;font-family:"Arvo",Georgia,serif;font-weight:400;font-size:40px;color:var(--white)}
.photo{position:absolute;width:333px;height:222px}
.ph-a{background:linear-gradient(135deg,#d9dde2,#6d7480 60%,#2a2e36)}
.ph-b{background:linear-gradient(135deg,#e8e6e0,#b9b4aa 55%,#5a5048)}
.ph-c{background:linear-gradient(135deg,#eef0f2,#a7b1bc 55%,#3c4654)}
.caption{position:absolute;top:430px;width:333px;text-align:center;font-family:"Arvo",Georgia,serif;font-size:17px;line-height:26px;color:var(--white)}
.services .btn{top:500px;height:50px}

/* blog */
.blog{height:492px;background:var(--grey)}
.blog h2,.address h2{position:absolute;left:0;right:0;text-align:center;font-family:"Arvo",Georgia,serif;font-weight:400;font-size:40px;color:var(--blue)}
.blog h2{top:58px}
.intro{position:absolute;left:190px;right:190px;text-align:center;font-size:13px;line-height:28px;color:#666}
.blog .intro{top:118px}
.blog .photo{top:200px}
.blog .overlay{position:absolute;inset:0;background:rgba(20,22,26,.72);padding:36px 26px;color:var(--white)}
.overlay h4{font-family:"Arvo",Georgia,serif;font-weight:400;font-size:17px}
.overlay .date{margin-top:10px;font-size:14px}
.overlay p{margin-top:10px;font-size:13px;line-height:27px}

/* address */
.address{height:201px;background:var(--white)}
.address .notch{top:0;border-top:32px solid var(--grey)}
.address h2{top:68px}
.address .intro{top:126px}

/* contact */
.contact{height:571px;display:flex}
.offices{width:601px;background:var(--blue);padding:72px 0 0 92px}
.office{position:relative;padding-left:48px;height:114px;color:var(--white)}
.office svg{position:absolute;left:0;top:0}
.office h4{font-family:"Arvo",Georgia,serif;font-weight:400;font-size:19px;margin-bottom:10px}
.office p{font-size:13px;line-height:28px}
.map{flex:1;background:linear-gradient(140deg,#ecebe4 0%,#e2e3da 50%,#d9dcd2 100%)}

/* footer */
.footer{height:188px;background:var(--footer);text-align:center}
.footer .follow{padding-top:42px;font-family:"Arvo",Georgia,serif;font-size:20px;color:#333}
.socials{margin-top:12px;display:flex;justify-content:center;gap:14px}
.socials span{width:32px;height:32px;background:var(--blue)}
.socials span:nth-child(2){background:#3aa3dc}
.socials span:nth-child(3){background:#2a8ac4}
.copy{margin-top:18px;font-size:12px;color:#555}
.copy b{color:var(--blue)}
</style>
</head>
<body>

<header class="hero">
  <div class="hero-photo" role="img" aria-label="Blurred office interior with a businessman in a suit, arms folded"></div>
  <nav class="nav">
    <a class="active">HOME</a><a>SERVICES</a><a>INVESTMENT APPROACH</a><a>MISSIONS AND VALUES</a><a>CONTACT</a>
  </nav>
  <div class="brand"><i class="dot"></i><span>CALLOWAY HOLDINGS</span></div>
  <h1>Lorem ipsum dolor sit amet</h1>
  <p>Fusce semper vitae leo sit amet vehicula.Lorem ipsum dolor sit amet, consectetur adipiscing elit. Fusce semper vitae leo sit amet vehicula.</p>
</header>

<section class="welcome">
  <div class="label">WELCOME TO</div>
  <h2>CALLOWAY HOLDINGS</h2>
  <p>Calloway Holdings is a is a boutique independent investment group that specializes in direct investments along with the provision of consulting and fund raising services to both established and emerging private companies. We are attracted to challenging assignments.</p>
  <a class="more">READ MORE</a>
  <div class="mark">CALLOWAY</div>
  <i class="notch"></i>
</section>

<section class="features">
  <div class="feature" style="left:80px">
    <div class="icon filled">
      <svg width="70" height="60" viewBox="0 0 70 60" fill="none" stroke="#fff" stroke-width="4"><path d="M6 30 L30 8 L54 30"/><path d="M14 26 V52 H34"/><circle cx="50" cy="42" r="13" fill="#fff" stroke="none"/><text x="50" y="49" text-anchor="middle" font-size="19" font-family="Arial" fill="#0255a3" stroke="none" font-weight="700">$</text></svg>
    </div>
    <h3 class="accent">OUR OWN FUNDS</h3>
    <p>Lorem Ipsum is simply dummy text of the printing and typesetting industry. Lorem Ipsum has been...</p>
  </div>
  <div class="feature" style="left:434px">
    <div class="icon">
      <svg width="60" height="54" viewBox="0 0 60 54" fill="#333"><ellipse cx="22" cy="44" rx="18" ry="6"/><rect x="4" y="34" width="36" height="10"/><ellipse cx="22" cy="34" rx="18" ry="6" fill="#666"/><ellipse cx="38" cy="24" rx="18" ry="6"/><rect x="20" y="12" width="36" height="12"/><ellipse cx="38" cy="12" rx="18" ry="6" fill="#666"/></svg>
    </div>
    <h3>INSTITUTIONAL INVESTOR</h3>
    <p>Lorem Ipsum is simply dummy text of the printing and typesetting industry. Lorem Ipsum has been...</p>
  </div>
  <div class="feature" style="left:788px">
    <div class="icon">
      <svg width="56" height="60" viewBox="0 0 56 60" fill="#333"><path d="M20 6 H36 L31 16 H25 Z"/><path d="M24 18 H32 C48 26 52 40 48 50 C45 56 11 56 8 50 C4 40 8 26 24 18 Z"/><text x="28" y="47" text-anchor="middle" font-size="20" font-family="Arial" fill="#fff" font-weight="700">$</text></svg>
    </div>
    <h3>ADVISORS &amp; CONSUITANTS</h3>
    <p>Lorem Ipsum is simply dummy text of the printing and typesetting industry. Lorem Ipsum has been...</p>
  </div>
  <a class="btn">SHOW ALL</a>
</section>

<section class="services">
  <i class="notch"></i>
  <div class="kicker">OUR</div>
  <h2>SERVICES</h2>
  <div class="photo ph-a" style="top:183px;left:78px" role="img" aria-label="Business people shaking hands in an office"></div>
  <div class="photo ph-b" style="top:183px;left:434px" role="img" aria-label="Businessman working at a desk with a laptop"></div>
  <div class="photo ph-c" style="top:183px;left:790px" role="img" aria-label="Two colleagues reviewing a tablet together"></div>
  <div class="caption" style="left:78px">ANGLE INVESTMENT</div>
  <div class="caption" style="left:434px">CAPITAL RAISINING</div>
  <div class="caption" style="left:790px">STRATEGIC BUSINESS<br>PLANNING</div>
  <a class="btn">SHOW ALL</a>
</section>

<section class="blog">
  <h2>BLOG</h2>
  <p class="intro">Lorem Ipsum is simply dummy text of the printing and typesetting industry. Lorem Ipsum has been the industry's standard dummy text ever.Lorem Ipsu.</p>
  <article class="photo ph-a" style="left:78px" role="img" aria-label="Business people meeting in an office">
    <div class="overlay">
      <h4>LOREM IPSUM SIMPLY</h4>
      <div class="date">10 Feb 2016</div>
      <p>Lorem Ipsum is simply dummy text of the printing and typesetting industry. Lorem Ipsum has been the.</p>
    </div>
  </article>
  <div class="photo ph-b" style="left:434px" role="img" aria-label="Businessman working at a desk with a laptop"></div>
  <div class="photo ph-c" style="left:790px" role="img" aria-label="Two colleagues reviewing a tablet together"></div>
</section>

<section class="address">
  <i class="notch"></i>
  <h2>ADDRESS</h2>
  <p class="intro">Lorem Ipsum is simply dummy text of the printing and typesetting industry. Lorem Ipsum has been the industry's standard dummy text ever.Lorem Ipsu.</p>
</section>

<section class="contact">
  <div class="offices">
    <div class="office"><svg width="22" height="30" viewBox="0 0 22 30"><path d="M11 0 C4.9 0 0 4.9 0 11 C0 19 11 30 11 30 C11 30 22 19 22 11 C22 4.9 17.1 0 11 0 Z" fill="#fff"/><circle cx="11" cy="11" r="4.5" fill="#0255a3"/></svg><h4>HONG KONG</h4><p>12f, 48 Harbour Crest Road, Central, Hong Kong<br>Telephone :&nbsp; +85230000000</p></div>
    <div class="office"><svg width="22" height="30" viewBox="0 0 22 30"><path d="M11 0 C4.9 0 0 4.9 0 11 C0 19 11 30 11 30 C11 30 22 19 22 11 C22 4.9 17.1 0 11 0 Z" fill="#fff"/><circle cx="11" cy="11" r="4.5" fill="#0255a3"/></svg><h4>HONG KONG</h4><p>12f, 48 Harbour Crest Road, Central, Hong Kong<br>Telephone :&nbsp; +85230000000</p></div>
    <div class="office"><svg width="22" height="30" viewBox="0 0 22 30"><path d="M11 0 C4.9 0 0 4.9 0 11 C0 19 11 30 11 30 C11 30 22 19 22 11 C22 4.9 17.1 0 11 0 Z" fill="#fff"/><circle cx="11" cy="11" r="4.5" fill="#0255a3"/></svg><h4>HONG KONG</h4><p>12f, 48 Harbour Crest Road, Central, Hong Kong<br>Telephone :&nbsp; +85230000000</p></div>
    <div class="office"><svg width="22" height="30" viewBox="0 0 22 30"><path d="M11 0 C4.9 0 0 4.9 0 11 C0 19 11 30 11 30 C11 30 22 19 22 11 C22 4.9 17.1 0 11 0 Z" fill="#fff"/><circle cx="11" cy="11" r="4.5" fill="#0255a3"/></svg><h4>HONG KONG</h4><p>12f, 48 Harbour Crest Road, Central, Hong Kong<br>Telephone :&nbsp; +85230000000</p></div>
  </div>
  <div class="map" role="img" aria-label="Street map showing the office location"></div>
</section>

<footer class="footer">
  <div class="follow">Follow US</div>
  <div class="socials"><span></span><span></span><span></span></div>
  <p class="copy">© 2016. <b>CALLOWAY HOLDINGS</b> All Rights Reserved.</p>
</footer>

</body>
</html>
```